Saddle Down at the Stable 2018

I need a flyer that can be printed in both 8.5x 11 and 11x17.
I have uploaded the flyer I used last year just to give you an idea of what I need
This event will include craft beer, live music and food trucks.
The silent auction is an important part of the evening.
It is a fundraiser for Meadow Stride Therapeutic Riding. (we teach horseback riding to special needs children and adults)
I will also need a tshirt design at some point so I would like the logo to be one that is suitable for a tshirt-the tshirt will be a dark color

Target Market(s)

ages 21-55 male and female
horse lovers

Industry/Entity Type

Horseback Riding

Font styles to use
Serif
Sans Serif

Colors

Designer to choose colors to be used in the design.

Requirements
Must have
• horse image
• similar information listed as on the flyer from last year
• second annual 2018
• information about the silent auction
• mention beer, food trucks, live music
• Wagon and Keg logo, lanternfield brewery logo
• November 3, 2018 6:oo-9:00 pm
• $25 ticket price which includes a flight of beer and an event tshirt
• www.mstrinc-example.com to purchase tickets
• Copperleaf Equestrian Center
• 5836 West Marigold Lane
• Woodstock, GA 30188
• barn logo
• email listed for more info: mstrinc@mailbox-example.com
Nice to have
• Please join us for a fundraiser to benefit Meadow Stride Therapeutic Riding, a non-profit organization that provides emotional, physical and social benefits for children and adults with special needs.
Should not have
• Mane Stride

```html
<!DOCTYPE html>
<html lang="en">
<head>
<meta charset="utf-8">
<title>Second Annual 2018 – Meadow Stride Fundraiser</title>
<link href="https://fonts.googleapis.com/css2?family=Oswald:wght@600;700&family=Playfair+Display:ital@1&family=Source+Sans+3:wght@400;600;700&display=swap" rel="stylesheet">
<style>
  :root{
    --red:#c8313a;
    --ink:#141414;
    --text:#1e1e1e;
    --grass-dark:#2f4a22;
    --grass:#6f8f4c;
    --grass-light:#a7b98a;
    --paper:#ffffff;
    --footer:#2a2a28;
    --tick:#6fb52e;
  }
  *{margin:0;padding:0;box-sizing:border-box}
  html,body{width:927px;height:1200px;overflow:hidden;background:#fff}
  .flyer{
    position:relative;width:927px;height:1200px;overflow:hidden;
    background:linear-gradient(to bottom,#fff 0,#fff 820px,#eeede6 960px,#c9c8bd 1100px,#8c8b82 1200px);
    font-family:"Source Sans 3",sans-serif;color:var(--text);
  }
  .hero-photo{
    position:absolute;left:0;top:0;width:927px;height:660px;
    background:linear-gradient(to bottom,#1f3317 0,var(--grass-dark) 140px,var(--grass) 300px,var(--grass-light) 460px,#dfe4d4 560px);
  }
  .hero-fade{
    position:absolute;left:0;top:0;width:927px;height:700px;
    background:
      radial-gradient(ellipse 360px 420px at 650px 470px,rgba(255,255,255,.95) 0,rgba(255,255,255,.8) 45%,rgba(255,255,255,0) 100%),
      linear-gradient(to bottom,rgba(255,255,255,0) 0,rgba(255,255,255,0) 460px,#fff 660px);
  }
  .org-mark{
    position:absolute;left:528px;top:67px;width:224px;height:224px;border-radius:50%;
    background:var(--paper);display:flex;flex-direction:column;align-items:center;justify-content:center;
    text-align:center;font-weight:700;font-size:17px;line-height:1.25;color:var(--ink);
    padding:0 26px;
  }
  .title{position:absolute;left:0;top:0;width:927px}
  .title-second{
    position:absolute;left:532px;top:322px;width:208px;text-align:center;
    font-family:"Oswald",sans-serif;font-weight:600;font-size:86px;line-height:1;color:var(--ink);letter-spacing:-2px;
  }
  .title-annual{
    position:absolute;left:440px;top:396px;width:396px;text-align:center;white-space:nowrap;
    font-family:"Oswald",sans-serif;font-weight:700;font-size:150px;line-height:1;color:var(--red);letter-spacing:-4px;
    transform:scaleX(.85);transform-origin:center;
  }
  .title-year{
    position:absolute;left:528px;top:522px;width:200px;text-align:center;
    font-family:"Playfair Display",serif;font-style:italic;font-size:66px;line-height:1;color:var(--ink);
  }
  .intro{position:absolute;left:92px;top:628px;width:650px;font-size:22px;line-height:31px}
  .intro strong{font-weight:700;font-size:24px;color:var(--ink)}
  .features{position:absolute;left:92px;top:786px;list-style:none}
  .feature{position:relative;height:45px;margin-bottom:7px;display:flex;align-items:center}
  .feature-tick{position:relative;z-index:2;width:32px;height:32px}
  .feature-label{
    margin-left:-12px;width:347px;height:45px;padding-left:32px;border-radius:7px;
    background:linear-gradient(to bottom,#d43a43,#b8262f);box-shadow:0 2px 3px rgba(0,0,0,.25);
    color:#fff;font-weight:700;font-size:28px;line-height:45px;text-transform:uppercase;
  }
  .details{position:absolute;left:487px;top:788px;list-style:none}
  .detail{display:flex;margin-bottom:14px}
  .detail-icon{width:40px;height:40px;margin-top:4px;flex:none}
  .detail-text{margin-left:23px;font-size:15px;line-height:19px;color:var(--text)}
  .detail-title{display:block;color:var(--red);font-weight:700;font-size:20px;line-height:24px;text-transform:uppercase}
  .sponsor{
    position:absolute;font-weight:700;font-size:19px;color:var(--ink);text-transform:uppercase;
    line-height:22px;text-align:center;
  }
  .sponsor-wagon{left:92px;top:1090px;width:164px}
  .sponsor-lantern{left:300px;top:1079px;width:146px}
  .contact{
    position:absolute;left:473px;top:1033px;width:454px;height:118px;border-top-left-radius:34px;
    background:var(--footer);color:#e8e8e8;padding:30px 0 0 79px;font-size:15px;line-height:19px;
  }
  .contact b{color:#fff;font-weight:700}
  .contact p+p{margin-top:10px}
  .base-band{position:absolute;left:0;top:1151px;width:927px;height:49px;background:linear-gradient(to bottom,#3b3b37,#1d1d1b)}
</style>
</head>
<body>
<main class="flyer">
  <div class="hero-photo" role="img" aria-label="Rider in a helmet on a dark horse galloping across a grass field with trees behind"></div>
  <div class="hero-fade"></div>

  <div class="org-mark">Copperleaf Equestrian Center<br>Meadow Stride Therapeutic Riding</div>

  <h1 class="title">
    <span class="title-second">SECOND</span>
    <span class="title-annual">ANNUAL</span>
    <span class="title-year">2018</span>
  </h1>

  <p class="intro"><strong>Please join us for a fundraiser to benefit<br>Meadow Stride Therapeutic Riding Center,</strong><br>a non-profit organization that provides emotional, physical and social benefits for children and adults with special needs.</p>

  <ul class="features">
    <li class="feature"><svg class="feature-tick" viewBox="0 0 32 32"><circle cx="16" cy="16" r="15" fill="var(--tick)"/><path d="M9 16.5l5 5 9-11" fill="none" stroke="#fff" stroke-width="3.5" stroke-linecap="round" stroke-linejoin="round"/></svg><span class="feature-label">Craft Beer Tasting</span></li>
    <li class="feature"><svg class="feature-tick" viewBox="0 0 32 32"><circle cx="16" cy="16" r="15" fill="var(--tick)"/><path d="M9 16.5l5 5 9-11" fill="none" stroke="#fff" stroke-width="3.5" stroke-linecap="round" stroke-linejoin="round"/></svg><span class="feature-label">Food Trucks</span></li>
    <li class="feature"><svg class="feature-tick" viewBox="0 0 32 32"><circle cx="16" cy="16" r="15" fill="var(--tick)"/><path d="M9 16.5l5 5 9-11" fill="none" stroke="#fff" stroke-width="3.5" stroke-linecap="round" stroke-linejoin="round"/></svg><span class="feature-label">Live Music</span></li>
    <li class="feature"><svg class="feature-tick" viewBox="0 0 32 32"><circle cx="16" cy="16" r="15" fill="var(--tick)"/><path d="M9 16.5l5 5 9-11" fill="none" stroke="#fff" stroke-width="3.5" stroke-linecap="round" stroke-linejoin="round"/></svg><span class="feature-label">Silent Auction</span></li>
  </ul>

  <ul class="details">
    <li class="detail">
      <svg class="detail-icon" viewBox="0 0 40 40"><circle cx="20" cy="20" r="17" fill="#f2a81d"/><circle cx="20" cy="20" r="12" fill="#fff"/><path d="M20 12v8l5 4" fill="none" stroke="#444" stroke-width="2.5" stroke-linecap="round"/></svg>
      <div class="detail-text"><span class="detail-title">November 3, 2018</span>6:00-9:00 pm</div>
    </li>
    <li class="detail">
      <svg class="detail-icon" viewBox="0 0 40 40"><path d="M4 34l8-10h16l8 10z" fill="#7fc3e8"/><path d="M20 4a7 7 0 0 0-7 7c0 6 7 13 7 13s7-7 7-13a7 7 0 0 0-7-7z" fill="#e0413a"/><circle cx="20" cy="11" r="2.6" fill="#fff"/></svg>
      <div class="detail-text"><span class="detail-title">Copperleaf Equestrian Center</span>5836 West Marigold Lane<br>Woodstock, GA 30188</div>
    </li>
    <li class="detail">
      <svg class="detail-icon" viewBox="0 0 40 40"><text x="20" y="31" text-anchor="middle" font-family="Source Sans 3, sans-serif" font-weight="700" font-size="34" fill="#3aa335">$</text><rect x="4" y="36" width="32" height="2" fill="#bbb"/></svg>
      <div class="detail-text"><span class="detail-title">$25 Ticket Price</span>which includes a flight of beer<br>and an event t-shirt</div>
    </li>
  </ul>

  <span class="sponsor sponsor-wagon">Wagon and Keg</span>
  <span class="sponsor sponsor-lantern">Lanternfield<br>Brewery</span>

  <div class="contact">
    <p>Please contact <b>mstrinc@mailbox-example.com</b><br>for more information</p>
    <p>Purchase tickets at <b>www.mstrinc-example.com</b></p>
  </div>
  <div class="base-band"></div>
</main>
</body>
</html>
```